Webdesign für Realisation von  Bannern für unterschiedliche Werbenetzwerke
Webdesign für Realisation von Bannern für unterschiedliche Werbenetzwerke
Zielgruppe
Wir bieten Planung und Realistion von HTML5 Bannern für unterschiedliche Werbenetzwerke (besonders Velmora Adpilot) an.
Zielgruppe sind Unternehmen, welche einfach und kostengünstig online Banner erstellt haben möchten.
Aufgabenstellung
Die Webseite soll ein Onepager werden.
Die Webseite soll dem beigefügten Logo angepasst werden.
Bestellung und Bestätigung soll als eine Art Layover dargestellt werden.
Die Seite soll folgendes beinhalten:
- Header mit Logo, Telefon/Kontakt/Bestellbutton
- Intro
- Information zu Banner und Zielgruppenausrichtung -> Remarketing / ähnliche Zielgruppen / Keywords / Webseiteninhalt / gemeinsame Interessen / Lebensereignisse (Hochschulabschluss, Umzug, Ehe, (alles vorher/nachher). Diese Informationen gerne textlich wie grafisch darstellen
- Information zum Bestellvorgang. Diese Informationen gerne textlich wie grafisch darstellen.
- Kalkulation mit Bestellung (Bestellung führt dann zum erwähnten Layover)
- Portfolio (Vorschau von z.B. 3 Banner plus Aufklappfunktion für weitere Vorschläge)
- Footer
Beispielseite
https://www.flinkwerbung-studio.de/
An der Struktur dieser Webseite würden wir uns gerne anlehnen. Zielmarkt wird jedoch die Deutschschweiz sein.

```html
<!DOCTYPE html>
<html lang="de">
<head>
<meta charset="utf-8">
<title>Bannerwerkstatt – HTML5-Banner</title>
<link rel="stylesheet" href="https://fonts.googleapis.com/css2?family=Fira+Sans+Condensed:wght@400;500;600&family=Carlito:wght@400;700&display=swap">
<style>
:root{
  --blue:#2b55c8;
  --blue-dark:#1f4aa8;
  --blue-text:#2459b6;
  --orange:#e8501f;
  --ink:#333a44;
  --muted:#6b717b;
  --gray-bg:#efeff1;
  --dark:#4a4a4c;
  --white:#fff;
}
*{box-sizing:border-box;margin:0;padding:0}
html,body{width:1200px;height:3352px;overflow:hidden}
body{position:relative;background:var(--white);font-family:"Carlito",sans-serif;color:var(--ink)}
.abs{position:absolute}
.btn{position:absolute;display:flex;align-items:center;justify-content:center;border-radius:16px;color:#fff;font-family:"Fira Sans Condensed",sans-serif;font-size:11px;letter-spacing:.2px;text-decoration:none}
.btn-orange{background:var(--orange)}
.btn-blue{background:var(--blue-dark)}

/* header */
.site-header{top:0;left:0;width:1200px;height:65px;background:#fff}
.brand{left:224px;top:12px;display:flex;align-items:center;gap:8px}
.brand-mark{width:38px;height:38px;background:var(--blue)}
.brand-name{font-family:"Fira Sans Condensed",sans-serif;font-weight:500;font-size:21px;color:var(--blue)}
.header-phone{right:335px;top:20px;text-align:right;font-size:10px;line-height:1.1}
.header-phone strong{font-size:12px;font-weight:400}

/* hero */
.hero{top:65px;left:0;width:1200px;height:365px;background:var(--blue)}
.hero h1{left:224px;top:88px;color:#fff;font-family:"Fira Sans Condensed",sans-serif;font-weight:500;font-size:28px;line-height:34px}
.hero p{left:224px;top:166px;width:420px;color:#fff;font-size:10.5px;line-height:16px}
.hero-devices{left:687px;top:153px;width:289px;height:302px;border-radius:10px;background:linear-gradient(160deg,#ffffff,#e6e9f2)}

/* features */
.section-title{left:0;width:1200px;text-align:center;color:var(--blue-text);font-family:"Fira Sans Condensed",sans-serif;font-weight:400;font-size:19px}
.section-sub{left:0;width:1200px;text-align:center;font-size:11px}
.feature{width:240px;text-align:center}
.feature svg{display:block;margin:0 auto 10px}
.feature h3{font-family:"Fira Sans Condensed",sans-serif;font-weight:500;font-size:11px;color:#222;margin-bottom:4px}
.feature p{font-size:10px;line-height:13px;color:var(--muted)}

/* what we do */
.about{top:807px;left:0;width:1200px;height:517px;background:var(--gray-bg)}
.about-photo{left:224px;top:58px;width:294px;height:404px;background:linear-gradient(135deg,#e9e4dc,#d6c9a8 55%,#b9c3cf)}
.about h2{left:536px;top:54px;font-family:"Fira Sans Condensed",sans-serif;font-weight:400;font-size:18px;color:#333}
.about .rule{left:536px;top:88px;width:48px;height:1px;background:#c8c8cc}
.about .txt{left:536px;width:438px;font-size:10px;line-height:15px;color:#444;text-align:justify}
.check-item{left:540px;width:430px;display:flex;gap:10px}
.check-item .dot{flex:none;width:20px;height:20px;border-radius:50%;background:#fff;display:flex;align-items:center;justify-content:center}
.check-item h4{font-size:11px;color:var(--blue-text);font-weight:700}
.check-item p{font-size:8.5px;line-height:11px;color:var(--muted)}

/* cost band */
.cost{top:1324px;left:0;width:1200px;height:227px;background:linear-gradient(120deg,#2d5bb5,#3e78cf 55%,#3267c2)}
.cost h2{left:0;width:1200px;top:48px;text-align:center;color:#fff;font-family:"Fira Sans Condensed",sans-serif;font-weight:400;font-size:23px}
.cost .rule{left:576px;top:84px;width:48px;height:2px;background:rgba(255,255,255,.6)}
.cost p{left:0;width:1200px;top:109px;text-align:center;color:#fff;font-size:12px}

/* steps */
.steps{top:1551px;left:0;width:1200px;height:470px;background:linear-gradient(180deg,#fff 0%,#f3f6fb 100%)}
.steps .kicker{left:224px;top:92px;font-size:11px}
.steps h2{left:224px;top:108px;color:var(--blue-text);font-family:"Fira Sans Condensed",sans-serif;font-weight:400;font-size:19px}
.steps p{left:224px;top:142px;width:526px;font-size:10.5px;line-height:18.7px;color:#444}
.step-card{width:116px;height:94px;background:#fff;box-shadow:0 1px 6px rgba(40,60,100,.12);display:flex;flex-direction:column;align-items:center;justify-content:flex-end;padding-bottom:10px;gap:8px}
.step-card span{font-size:11px;color:var(--blue-text)}

/* portfolio */
.work-tile{width:191px;height:191px}

/* pricing */
.pricing{top:2649px;left:0;width:1200px;height:540px;background:linear-gradient(180deg,#f7f7f8,#e9e8e6 60%,#f3f2f0)}
.benefits{left:225px;top:65px;width:320px;height:260px;background:#e4e4e6}
.benefits-head{height:72px;background:var(--blue-dark);color:#fff;display:flex;align-items:center;gap:12px;padding:0 14px;position:relative}
.benefits-head small{display:block;font-size:10.5px}
.benefits-head strong{font-family:"Fira Sans Condensed",sans-serif;font-size:18px;font-weight:500}
.arrow-down{position:absolute;bottom:-12px;left:50%;margin-left:-12px;border:12px solid transparent;border-bottom:0}
.benefits ul{list-style:none;padding:18px 16px 0 16px;font-size:10.5px;line-height:13px}
.benefits li{display:flex;gap:6px;margin-bottom:6px}
.benefits .note{padding:10px 16px;font-size:10.5px;line-height:14px}
.calc{left:575px;top:65px;width:322px;height:403px;background:var(--dark)}
.calc-head{height:56px;background:var(--orange);color:#fff;display:flex;align-items:center;gap:12px;padding:0 20px;position:relative}
.calc-head strong{font-family:"Fira Sans Condensed",sans-serif;font-size:18px;font-weight:500}
.calc-body{position:absolute;left:8px;top:82px;width:306px;height:208px;background:#ececee;font-size:14px;color:#333}
.q{position:absolute;left:10px;display:flex;align-items:center;gap:8px}
.q-num{width:16px;height:16px;border-radius:50%;background:#fff;font-size:9px;display:flex;align-items:center;justify-content:center}
.opt{position:absolute;font-size:11px;display:flex;align-items:center;gap:6px}
.box{width:14px;height:12px;background:#fff;border:1px solid #ccc}
.radio{width:11px;height:11px;border-radius:50%;border:1px solid #999;background:#fff}
.calc-price{position:absolute;left:20px;right:30px;top:305px;color:#fff;display:flex;justify-content:space-between}
.calc-price .label{font-size:14px}
.calc-price small{display:block;font-size:7px;margin-top:2px}
.calc-price .val{text-align:right;font-size:13px}

/* footer */
.site-footer{top:3189px;left:0;width:1200px;height:163px;background:var(--blue-dark);color:#fff}
.site-footer h4{left:224px;top:40px;font-family:"Fira Sans Condensed",sans-serif;font-weight:500;font-size:11px}
.site-footer p{left:224px;top:64px;width:330px;font-size:10px;line-height:13px}
.footer-contact{right:226px;top:32px;text-align:right;font-size:11px}
.footer-contact strong{display:block;font-size:17px;font-weight:700}
.socials{right:226px;top:92px;display:flex;gap:8px}
.socials i{width:13px;height:13px;border-radius:50%;background:#fff;display:block}
.copy{right:226px;top:119px;font-size:10px}
</style>
</head>
<body>

<header class="site-header abs">
  <div class="brand abs"><span class="brand-mark"></span><span class="brand-name">BANNERWERKSTATT</span></div>
  <div class="header-phone abs">Ruf uns an<br><strong>(800) 555-0142</strong></div>
  <a class="btn btn-orange" style="left:883px;top:19px;width:91px;height:26px;font-size:12px">Jetzt bestellen</a>
</header>

<section class="hero abs">
  <h1 class="abs">Schaffung. Anpassung. Lokalisierung.<br>Kampagnen in HTML5</h1>
  <p class="abs">Online-Werbung ohne langwierige, schwierige Prozesse &amp; ganz ohne Produktionskosten. Voll animierte, Velmora Adpilot-freundliche HTML5-Bannerwerbung - mit Velmora Studio (VST). HTML5-Banner können als Responsive gestaltet werden, mit vielen interessanten Funktionen, die auf jedem Gerät ausgeführt werden können.</p>
  <a class="btn btn-orange" style="left:224px;top:252px;width:124px;height:29px">BERECHNEN SIE JETZT</a>
</section>
<div class="hero-devices abs" role="img" aria-label="Tablet und Smartphone mit responsiven Banner-Beispielen"></div>

<h2 class="section-title abs" style="top:518px">SCHÖNE HTML5- UND RICH-MEDIA-WERBEBANNER</h2>
<p class="section-sub abs" style="top:541px">Erreichen Sie die maximale Wirkung Ihrer digitalen Marketingkampagne</p>

<div class="feature abs" style="left:233px;top:610px">
  <svg width="72" height="46" viewBox="0 0 72 46" fill="none" stroke="#333" stroke-width="2"><rect x="8" y="3" width="44" height="30" rx="2"/><path d="M2 38h56"/><rect x="52" y="16" width="16" height="26" rx="2"/><rect x="38" y="22" width="12" height="20" rx="2"/></svg>
  <h3>WERBEN SIE ÜBERALL</h3>
  <p>Unsere Banner laufen auf allen Geräten<br>und über alle Medien hinweg.</p>
</div>
<div class="feature abs" style="left:477px;top:610px">
  <svg width="74" height="46" viewBox="0 0 74 46" fill="#333"><rect x="2" y="18" width="14" height="4"/><rect x="2" y="25" width="14" height="4"/><rect x="2" y="32" width="14" height="4"/><rect x="20" y="6" width="14" height="4"/><rect x="20" y="13" width="14" height="4"/><rect x="20" y="20" width="14" height="4"/><circle cx="37" cy="34" r="9"/><rect x="48" y="18" width="14" height="4"/><rect x="48" y="25" width="14" height="4"/><rect x="48" y="32" width="24" height="4"/><rect x="2" y="39" width="70" height="4"/></svg>
  <h3>KOSTENEFFIZIENT</h3>
  <p>Wir berechnen für das Hosting, aber nur,<br>wenn Ihre Kampagne bereit ist.</p>
</div>
<div class="feature abs" style="left:725px;top:608px">
  <svg width="52" height="48" viewBox="0 0 52 48" fill="#333" stroke="#333" stroke-width="2.5"><path d="M26 24 8 8M26 24 44 8M26 24 8 40M26 24 44 40M26 24h20"/><circle cx="26" cy="24" r="7"/><circle cx="8" cy="8" r="4"/><circle cx="44" cy="8" r="4"/><circle cx="8" cy="40" r="4"/><circle cx="44" cy="40" r="4"/><circle cx="48" cy="24" r="3"/></svg>
  <h3>NETZWERKFREUNDLICH</h3>
  <p>Kompatibel mit allen größeren Netzwerken,<br>einschließlich Klarnetz, Werbeknoten und Velmora.</p>
</div>

<section class="about abs">
  <div class="about-photo abs" role="img" aria-label="Foto: Team arbeitet gemeinsam an einem Bildschirm"></div>
  <h2 class="abs">Was wir tun</h2>
  <div class="rule abs"></div>
  <p class="txt abs" style="top:108px">Wir bieten hochwertige und kreative Lösungen für digitale Bannerwerbung, die auf Ihre Marketingkampagne zugeschnitten sind. Unser Team hat Hunderte von Banner-Werbekampagnen entwickelt und implementiert, und die Lösungen werden von den globalen Marken und Werbeagenturen geschätzt.</p>
  <p class="txt abs" style="top:183px">Von der Erstellung über die Anpassung bis hin zur Erstellung von synchronisierten Rich Media-Bannern mit mehreren Einheiten - wir nehmen das Gewicht der Bannerproduktion von Ihrer Schulter. Senden Sie uns das kreative Storyboard oder die Kampagneninhalte in einem gängigen Format (PSD, AI usw.) und wir liefern qualitativ hochwertige, inspirierende HTML5-Bannerwerbung innerhalb kürzester Zeit.</p>
  <div class="check-item abs" style="top:285px"><span class="dot"><svg width="10" height="8" viewBox="0 0 10 8"><path d="M1 4l3 3 5-6" stroke="#2459b6" stroke-width="1.6" fill="none"/></svg></span><div><h4>Gefertigtes Storyboard</h4><p>Entwerfen Sie ein schönes Storyboard, um Ihre Marke und Marketinginhalte effektiv zu präsentieren. Unser detailliertes Design bietet den perfekten Überblick über Animation und Interaktivität.</p></div></div>
  <div class="check-item abs" style="top:341px"><span class="dot"><svg width="10" height="8" viewBox="0 0 10 8"><path d="M1 4l3 3 5-6" stroke="#2459b6" stroke-width="1.6" fill="none"/></svg></span><div><h4>Große Auswahl an Bannern</h4><p>Standard, Rich-Media, Übernahme, Behaviour-Targeting mit dynamischem Feed - wir können jede Art von digitaler Bannerwerbung erstellen, die Sie sich vorstellen und in alle wichtigen Werbeplattformen integrieren können.</p></div></div>
  <div class="check-item abs" style="top:403px"><span class="dot"><svg width="10" height="8" viewBox="0 0 10 8"><path d="M1 4l3 3 5-6" stroke="#2459b6" stroke-width="1.6" fill="none"/></svg></span><div><h4>Großserienproduktion</h4><p>Konvertieren Sie das Design in eine elegante HTML5-Banneranzeige. Wir adaptieren, skalieren und lokalisieren Banners, um die Reichweite Ihrer digitalen Marketingkampagne regional und global zu erweitern.</p></div></div>
</section>

<section class="cost abs" role="img" aria-label="Hintergrundfoto: Hände an einer Laptop-Tastatur, blau eingefärbt">
  <h2 class="abs">WIE VIEL KOSTET MEIN BANNER?</h2>
  <div class="rule abs"></div>
  <p class="abs">Berechnen Sie Ihre Banner-Projektkosten mit diesem interaktiven Tool.</p>
  <a class="btn btn-orange" style="left:542px;top:149px;width:116px;height:29px">BERECHNEN SIE JETZT</a>
</section>

<section class="steps abs">
  <p class="kicker abs">Und so einfach geht´s</p>
  <h2 class="abs">IN FÜNF SCHRITTEN ZUM FERTIGEN HTML5-BANNER</h2>
  <p class="abs">Im persönlichen Gespräch definieren wir gemeinsam Ihre Ziele. An welche Zielgruppe möchten Sie welches Produkt vermarkten? Wie ist Ihr Zeitplan und wie Ihr Budget? Gemeinsam planen wir die Bannerkampagne nach Ihren Wünschen. Nach unserem Gespräch erstellen wir Ihnen ein Angebot mit verlässlichen Festpreisen. Jetzt geht es ins Detail! Wir entwickeln kreative Ideen, um Ihre Inhalte umzusetzen. Dabei behalten wir immer Ihren Zeitplan und Ihr Budget im Auge. Wir finden die optimale Lösung für Ihr Produkt. Mit aktuellster Technik programmieren wir Ihre Werbebanner sorgfältig und individuell. Natürlich erfüllen unsere animierten HTML5-Banner alle Anforderungen Ihres Werbenetzwerkes. Auf Wunsch übermitteln wir die Daten auch direkt an Ihren Mediapartner oder Publisher.</p>
  <a class="btn btn-blue" style="left:227px;top:312px;width:115px;height:29px;font-size:10px">BERECHNEN SIE JETZT</a>

  <div class="step-card abs" style="left:795px;top:47px"><svg width="42" height="46" viewBox="0 0 42 46" fill="none" stroke="#2459b6" stroke-width="2"><rect x="8" y="2" width="26" height="34" rx="2"/><path d="M14 10h14M14 16h14M14 22h10"/><path d="M2 30h38v10H2z"/></svg><span>Umsetzung</span></div>
  <div class="step-card abs" style="left:1049px;top:52px"><svg width="46" height="46" viewBox="0 0 46 46" fill="none" stroke="#2459b6" stroke-width="2"><rect x="18" y="2" width="26" height="20" rx="2"/><path d="M22 8h18M22 14h14"/><rect x="2" y="16" width="20" height="16" rx="2"/><circle cx="16" cy="38" r="4"/><path d="M8 44h16"/></svg><span>Feedback</span></div>
  <div class="step-card abs" style="left:920px;top:156px"><svg width="54" height="40" viewBox="0 0 54 40" fill="none" stroke="#2459b6" stroke-width="2"><rect x="4" y="4" width="46" height="26" rx="2"/><path d="M2 34h50M14 12h26M14 20h18"/></svg><span>Auslieferung</span></div>
  <div class="step-card abs" style="left:795px;top:258px"><svg width="46" height="46" viewBox="0 0 46 46" fill="none" stroke="#2459b6" stroke-width="2"><circle cx="14" cy="14" r="10"/><path d="M10 24v6h8v-6M24 22c6-4 14-2 16 4s-2 12-8 12H22"/><path d="M22 30h10"/></svg><span>Beratung</span></div>
  <div class="step-card abs" style="left:1049px;top:258px"><svg width="42" height="48" viewBox="0 0 42 48" fill="none" stroke="#2459b6" stroke-width="2"><rect x="4" y="6" width="34" height="38" rx="2"/><rect x="10" y="2" width="22" height="30" rx="2"/><path d="M21 6v18"/></svg><span>Vorschlag</span></div>
</section>

<h2 class="section-title abs" style="top:2068px">AUSGEWÄHLTE ARBEIT</h2>
<p class="section-sub abs" style="top:2094px;left:320px;width:560px;line-height:13px;font-size:10.5px">Beautiful Banner Ads werden mit viel Liebe und Liebe zum Detail erstellt. Das folgende Kunstwerk und die endgültige Ausgabe sind Eigentum der relevanten Marken und Werbeagenturen.</p>

<div class="work-tile abs" style="left:211px;top:2158px;background:linear-gradient(160deg,#3a0a0a,#a81818)" role="img" aria-label="Kinoplakat-Banner in Rot und Schwarz"></div>
<div class="work-tile abs" style="left:415px;top:2158px;background:linear-gradient(180deg,#d9d9d9,#3c3c3c)" role="img" aria-label="Serien-Banner in Grautönen"></div>
<div class="work-tile abs" style="left:621px;top:2158px;background:linear-gradient(180deg,#f7d6dc,#e65a7c)" role="img" aria-label="Weihnachts-Restaurantbanner in Rosa"></div>
<div class="work-tile abs" style="left:825px;top:2158px;background:linear-gradient(160deg,#ffffff,#f3d4d8)" role="img" aria-label="Frühlingsbanner mit rotem Schriftzeichen auf Weiß"></div>
<div class="work-tile abs" style="left:211px;top:2384px;background:linear-gradient(180deg,#ececec,#5a5f66 55%,#1b1b1b)" role="img" aria-label="Film-Veröffentlichungsbanner in Grau und Rot"></div>
<div class="work-tile abs" style="left:415px;top:2384px;background:linear-gradient(160deg,#2fa35a,#e8e2d0 60%,#d8342a)" role="img" aria-label="Spielbanner mit Comicfigur"></div>
<div class="work-tile abs" style="left:621px;top:2384px;background:linear-gradient(180deg,#1c2a6e,#2c1d5c)" role="img" aria-label="Musical-Ticketbanner in Dunkelblau und Pink"></div>
<div class="work-tile abs" style="left:825px;top:2384px;background:linear-gradient(180deg,#f3f3f3,#d4d4d4)" role="img" aria-label="Laptop-Produktbanner in Hellgrau"></div>

<section class="pricing abs" role="img" aria-label="Heller Schreibtisch-Hintergrund mit Lampe und Brille">
  <div class="benefits abs">
    <div class="benefits-head">
      <svg width="40" height="40" viewBox="0 0 40 40" fill="none" stroke="#fff" stroke-width="2"><rect x="3" y="5" width="34" height="24"/><path d="M10 22v-6M16 22v-10M22 22v-4M28 22v-8M20 29v6M12 38h16"/></svg>
      <div><small>HTML5-Banner zu Festpreisen</small><strong>Ihre Vorteile auf einen Blick</strong></div>
      <span class="arrow-down" style="border-top-color:var(--blue-dark)"></span>
    </div>
    <ul>
      <li><svg width="10" height="10" viewBox="0 0 10 8"><path d="M1 4l3 3 5-6" stroke="#2459b6" stroke-width="1.5" fill="none"/></svg>Persönliche Beratung</li>
      <li><svg width="10" height="10" viewBox="0 0 10 8"><path d="M1 4l3 3 5-6" stroke="#2459b6" stroke-width="1.5" fill="none"/></svg>Entwicklung nach Vorgaben Ihrer Werbenetzwerke</li>
      <li><svg width="10" height="10" viewBox="0 0 10 8" style="flex:none"><path d="M1 4l3 3 5-6" stroke="#2459b6" stroke-width="1.5" fill="none"/></svg><span>Auf Wunsch direkte Lieferung an Ihre Mediaagentur oder Publisher wie Velmora Display, Zielklick, Rollnetz, Klarnetz</span></li>
    </ul>
    <p class="note">Mit unseren Festpreisen bleiben Sie immer im Budget. Die folgenden Preise sind für Standardformate. Natürlich machen wir Ihnen auch gerne ein persönliches Angebot für Sonderformate, Interaktion und Rich Media.</p>
  </div>

  <div class="calc abs">
    <div class="calc-head">
      <span style="width:32px;height:32px;border:2px solid #fff;display:block"></span>
      <strong>HTML5 Banner</strong>
      <span class="arrow-down" style="border-top-color:var(--orange)"></span>
    </div>
    <div class="calc-body">
      <div class="q" style="top:20px"><span class="q-num">1</span>Designstudie enthalten</div>
      <div class="opt" style="left:36px;top:48px"><span class="radio" style="box-shadow:inset 0 0 0 3px #fff;background:#2459b6"></span>Ja</div>
      <div class="opt" style="left:78px;top:48px"><span class="radio"></span>Nein</div>
      <div class="q" style="top:97px"><span class="q-num">2</span>Wie viele Banner-Größen benötigen Sie?</div>
      <div class="opt" style="left:34px;top:128px"><span class="box"></span>1</div>
      <div class="opt" style="left:74px;top:128px"><span class="box"></span>2</div>
      <div class="opt" style="left:113px;top:128px"><span class="box"></span>3</div>
      <div class="opt" style="left:153px;top:128px"><span class="box"></span>4</div>
      <div class="opt" style="left:193px;top:128px"><span class="box"></span>5</div>
      <div class="opt" style="left:233px;top:128px"><span class="box"></span>6</div>
      <div class="opt" style="left:34px;top:159px"><span class="box"></span>7</div>
      <div class="opt" style="left:74px;top:159px"><span class="box"></span>8</div>
      <div class="opt" style="left:113px;top:159px"><span class="box"></span>9</div>
      <div class="opt" style="left:153px;top:159px;color:#2459b6"><span class="box" style="border-color:#2459b6;display:flex;align-items:center;justify-content:center"><svg width="10" height="8" viewBox="0 0 10 8"><path d="M1 4l3 3 5-6" stroke="#2459b6" stroke-width="1.5" fill="none"/></svg></span>10</div>
      <div class="opt" style="left:193px;top:159px"><span class="box"></span>11</div>
      <div class="opt" style="left:233px;top:159px"><span class="box"></span>12</div>
    </div>
    <div class="calc-price">
      <div class="label">Kampagnenprei<small>VAT 7,7% MWST</small></div>
      <div class="val">391,00 € *<small>74,29 €</small></div>
    </div>
    <a class="btn" style="left:16px;top:358px;width:270px;height:28px;background:#6b6b6d;color:#fff;font-size:10px">JETZT UNVERBINDLICH ANFRAGEN</a>
  </div>
</section>

<footer class="site-footer abs">
  <h4 class="abs">MEHR ÜBER UNS</h4>
  <p class="abs">Lorem ipsum dolor sit amet, consectetur adipiscing elit, sed do eiusmod tempor incididunt ut labore et dolore magna aliqua. Ut enim ad minim veniam, quis nostrud exercitation ullamco laboris nisi ut aliquip ex ea commodo consequat.</p>
  <div class="footer-contact abs">Ruf uns an<strong>(800) 555-0142</strong></div>
  <div class="socials abs"><i></i><i></i><i></i><i></i></div>
  <div class="copy abs">@ 2018 BANNERWERKSTATT</div>
</footer>

</body>
</html>
```